Full service meeting planning company needs new business cards

Velmora Linkway is a full service meeting planning company that specializes in on-line conference registration web development and event communications. We combine citywide hotel management, mobile applications, eblast reminders, confirmation letters, and customized reporting to create a seamless registration process. We also manage group motor coach transportation, food and beverages, entertainment, stage and lighting for group of 10 to 4000.

Target Market(s)

Corporations and associations

Industry/Entity Type

Event Planning

Contact Information for Business Card

standard size 3.5" wide and 2" tall

Font styles to use
Serif
Sans Serif

Colors
f37122
f78f20
333333
5c5c5c
9d9d9d
f68d4d

Requirements
Must have
• {name}
• Velmora Linkway
• P.O. Box 7384, Grand Rapids, M I 49568
• www.velmoralinkway.com
• {email}
• {phone}
• {mobile phone}
Nice to have
• Our colors are black, grey and orange as an accent color
Should not have
• I am not happy with our website layout anymore either. It feels dark and old but it does explain who we are pretty well if you'd like to review; www.velmoralinkway.com

```html
<!DOCTYPE html>
<html lang="en">
<head>
<meta charset="utf-8">
<title>Velmora Linkway – Business Cards</title>
<link rel="stylesheet" href="https://fonts.googleapis.com/css2?family=Jost:wght@500&family=Libre+Baskerville:wght@400;700&family=Roboto+Condensed:wght@400&display=swap">
<style>
  :root {
    --orange: #f37122;
    --orange-light: #f78f20;
    --orange-soft: #f68d4d;
    --ink: #333333;
    --ink-mid: #5c5c5c;
    --ink-light: #9d9d9d;
    --paper: #ffffff;
    --backdrop: #e9e9ea;
  }
  * { box-sizing: border-box; margin: 0; padding: 0; }
  html, body { width: 1200px; height: 900px; overflow: hidden; }
  body {
    background: var(--backdrop);
    display: flex;
    flex-direction: column;
    align-items: center;
    justify-content: center;
    gap: 24px;
  }
  .card {
    position: relative;
    width: 700px;
    height: 400px;
    background: var(--paper);
    border-radius: 26px;
    overflow: hidden;
    box-shadow: 0 6px 18px rgba(0,0,0,0.12);
  }
  .pattern-band {
    position: absolute;
    left: 0;
    background: linear-gradient(90deg, var(--orange-soft) 0%, #fbc7a6 100%);
  }

  /* Contact side */
  .card--contact .panel {
    position: absolute;
    inset: 0;
    background: linear-gradient(135deg, var(--orange) 0%, var(--orange-light) 100%);
    clip-path: polygon(0 0, 440px 0, 340px 342px, 0 342px);
  }
  .card--contact .pattern-band { bottom: 0; width: 340px; height: 58px; }
  .card--contact .base-band {
    position: absolute; left: 340px; right: 0; bottom: 0; height: 22px;
    background: var(--orange);
  }
  .card--contact .company {
    position: absolute; left: 34px; top: 36px;
    font-family: "Jost", sans-serif; font-weight: 500;
    font-size: 34px; letter-spacing: 1px; text-transform: uppercase;
    color: var(--paper);
  }
  .card--contact .rule {
    position: absolute; left: 34px; top: 88px; width: 368px; height: 3px;
    background: var(--paper);
  }
  .contact-list {
    position: absolute; left: 38px; top: 124px;
    list-style: none;
    font-family: "Roboto Condensed", sans-serif; font-size: 17px;
    color: var(--paper);
  }
  .contact-list li { display: flex; align-items: center; gap: 12px; height: 32px; }
  .contact-list svg { width: 16px; height: 16px; flex: none; }
  .card--contact .mark {
    position: absolute; left: 440px; top: 100px; width: 240px;
    display: flex; flex-direction: column; align-items: center; gap: 14px;
  }
  .mark-dot { width: 120px; height: 120px; border-radius: 50%; background: var(--orange); }
  .mark-name {
    font-family: "Jost", sans-serif; font-weight: 500; font-size: 20px;
    letter-spacing: 1px; text-transform: uppercase; color: var(--orange);
  }

  /* Name side */
  .card--name .brand {
    position: absolute; left: 44px; top: 44px;
    display: flex; align-items: center; gap: 22px;
  }
  .card--name .brand .mark-dot { width: 96px; height: 96px; }
  .card--name .brand .mark-name { font-size: 32px; }
  .card--name .pattern-band { bottom: 0; width: 420px; height: 56px; }
  .card--name .base-band {
    position: absolute; left: 420px; right: 0; bottom: 0; height: 22px;
    background: var(--orange);
  }
  .card--name .corner-block {
    position: absolute; right: 0; bottom: 0; width: 60px; height: 70px;
    background: var(--orange);
  }
  .person {
    position: absolute; right: 84px; bottom: 96px; text-align: right;
    font-family: "Libre Baskerville", serif;
  }
  .person-name { font-size: 30px; font-weight: 700; color: #111; text-transform: uppercase; letter-spacing: 1px; line-height: 1.2; }
  .person-title { font-size: 19px; color: var(--ink-mid); margin-top: 6px; line-height: 1.2; }
</style>
</head>
<body>
  <section class="card card--contact">
    <div class="panel"></div>
    <div class="pattern-band" role="img" aria-label="Decorative diagonal stripe band in orange and white"></div>
    <div class="base-band"></div>
    <h2 class="company">Velmora Linkway</h2>
    <div class="rule"></div>
    <ul class="contact-list">
      <li>
        <svg viewBox="0 0 16 16" fill="none" stroke="currentColor" stroke-width="1.4"><rect x="4" y="1" width="8" height="14" rx="1.5"/><line x1="7" y1="12.5" x2="9" y2="12.5"/></svg>
        (616) 555-0142
      </li>
      <li>
        <svg viewBox="0 0 16 16" fill="none" stroke="currentColor" stroke-width="1.4"><path d="M3 2h3l1.5 3.5-2 1.3a8 8 0 0 0 3.7 3.7l1.3-2L14 10v3a1 1 0 0 1-1 1A11 11 0 0 1 2 3a1 1 0 0 1 1-1z"/></svg>
        (616) 555-0187
      </li>
      <li>
        <svg viewBox="0 0 16 16" fill="none" stroke="currentColor" stroke-width="1.4"><rect x="1.5" y="3.5" width="13" height="9"/><path d="M1.5 3.5 8 9l6.5-5.5"/></svg>
        info@velmoralinkway.com
      </li>
      <li>
        <svg viewBox="0 0 16 16" fill="none" stroke="currentColor" stroke-width="1.3"><circle cx="8" cy="8" r="6.5"/><ellipse cx="8" cy="8" rx="3" ry="6.5"/><line x1="1.5" y1="8" x2="14.5" y2="8"/></svg>
        www.velmoralinkway.com
      </li>
      <li>
        <svg viewBox="0 0 16 16" fill="none" stroke="currentColor" stroke-width="1.4"><path d="M8 15s5-5 5-8.5a5 5 0 0 0-10 0C3 10 8 15 8 15z"/><circle cx="8" cy="6.5" r="1.8"/></svg>
        P.O. Box 7384, Grand Rapids, M I 49568
      </li>
    </ul>
    <div class="mark">
      <div class="mark-dot"></div>
      <span class="mark-name">Velmora Linkway</span>
    </div>
  </section>

  <section class="card card--name">
    <div class="brand">
      <div class="mark-dot"></div>
      <span class="mark-name">Velmora Linkway</span>
    </div>
    <div class="person">
      <p class="person-name">Daniel Harwick</p>
      <p class="person-title">Event Manager</p>
    </div>
    <div class="pattern-band" role="img" aria-label="Decorative diagonal stripe band in orange and white"></div>
    <div class="base-band"></div>
    <div class="corner-block"></div>
  </section>
</body>
</html>
```